Business Card Design

I need a business card design for my new solo law practice. I practice consumer bankruptcy law.

I would like a simple, functional business card that looks professional but will also be understandable to regular people - not just other lawyers.
Updates

I added a couple of possible logos that can be incorporated

I'm sorry about the confusion, but the suite number for my new office is suite #150. Thanks for your patience

Target Market(s)

the real target market is potential clients

Industry/Entity Type

Business

Contact Information for Business Card

Law Offices of Dorian P. Whitcombe
Dorian P. Whitcombe
Attorney at Law
Bankruptcy Law
487 Mariner Court #150
Elmbrook, OR 97999
(555) 318-7264 (Phone)
(555) 318-7290 (Fax)
dorianw@fernleydebtrelief.example
fernleydebtrelief.example

Font styles to use
Serif

Requirements
Nice to have
• I've added some possible logos to possible incorporate

```html
<!DOCTYPE html>
<html lang="en">
<head>
<meta charset="utf-8">
<title>Dorian P. Whitcombe – Business Card</title>
<link rel="stylesheet" href="https://fonts.googleapis.com/css2?family=Open+Sans:wght@400;600&display=swap">
<style>
  :root {
    --brand-blue: #1c5aa8;
    --card-white: #ffffff;
    --backdrop: #e9e9ec;
    --text-light: #ffffff;
  }
  * { box-sizing: border-box; margin: 0; padding: 0; }
  html, body {
    width: 1200px;
    height: 564px;
    overflow: hidden;
    background: var(--backdrop);
    font-family: "Open Sans", sans-serif;
  }
  .stage {
    width: 1200px;
    height: 564px;
    display: flex;
    align-items: center;
    justify-content: center;
  }
  .business-card {
    position: relative;
    width: 840px;
    height: 480px;
    border-radius: 34px;
    overflow: hidden;
    display: flex;
    background: var(--card-white);
    box-shadow: 0 6px 18px rgba(0, 0, 0, 0.18);
  }
  .identity-panel {
    width: 64%;
    height: 100%;
    background: var(--brand-blue);
    color: var(--text-light);
    padding: 96px 0 0 44px;
    display: flex;
    flex-direction: column;
  }
  .attorney-name {
    font-size: 38px;
    font-weight: 400;
    letter-spacing: 0.5px;
    line-height: 1;
    text-transform: uppercase;
    white-space: nowrap;
  }
  .attorney-title {
    margin-top: 8px;
    font-size: 17px;
    font-weight: 600;
  }
  .contact-list {
    list-style: none;
    margin-top: auto;
    margin-bottom: 38px;
  }
  .contact-item {
    display: flex;
    align-items: center;
    gap: 14px;
    font-size: 20px;
    line-height: 1.6;
    white-space: nowrap;
  }
  .contact-icon {
    width: 16px;
    height: 16px;
    flex: none;
    fill: var(--text-light);
  }
  .address-panel {
    flex: 1;
    display: flex;
    align-items: flex-end;
    padding: 0 0 130px 34px;
  }
  .office-address {
    font-style: normal;
    color: var(--brand-blue);
    font-size: 28px;
    line-height: 1.3;
    white-space: nowrap;
  }
</style>
</head>
<body>
<main class="stage">
  <article class="business-card">
    <section class="identity-panel">
      <h1 class="attorney-name">Dorian P. Whitcombe</h1>
      <p class="attorney-title">Attorney at Law Bankruptcy Law</p>
      <ul class="contact-list">
        <li class="contact-item">
          <svg class="contact-icon" viewBox="0 0 16 16" aria-hidden="true"><rect x="4" y="1" width="8" height="14" rx="1.5"/><rect x="5.5" y="3" width="5" height="8" fill="#1c5aa8"/></svg>
          <span>(555) 318-7264</span>
        </li>
        <li class="contact-item">
          <svg class="contact-icon" viewBox="0 0 16 16" aria-hidden="true"><rect x="4" y="1" width="8" height="5"/><rect x="1" y="6" width="14" height="9" rx="1.5"/><rect x="4" y="9" width="8" height="3" fill="#1c5aa8"/></svg>
          <span>(555) 318-7290</span>
        </li>
        <li class="contact-item">
          <svg class="contact-icon" viewBox="0 0 16 16" aria-hidden="true"><rect x="1" y="3" width="14" height="10" rx="1"/><path d="M1.5 3.8 8 9l6.5-5.2" fill="none" stroke="#1c5aa8" stroke-width="1.4"/></svg>
          <span>dorianw@fernleydebtrelief.example</span>
        </li>
        <li class="contact-item">
          <svg class="contact-icon" viewBox="0 0 16 16" aria-hidden="true"><circle cx="8" cy="8" r="7"/><path d="M1 8h14M8 1c-3 3.5-3 10.5 0 14M8 1c3 3.5 3 10.5 0 14" fill="none" stroke="#1c5aa8" stroke-width="1.2"/></svg>
          <span>www.fernleydebtrelief.example</span>
        </li>
      </ul>
    </section>
    <section class="address-panel">
      <address class="office-address">
        487 Mariner Court<br>
        #150 Elmbrook,<br>
        OR 97999
      </address>
    </section>
  </article>
</main>
</body>
</html>
```